TRV Flyer

We need a professional design for flyers that we produce. The attached event draft is typical of the majority of flyers we will produce, and is the one that we need to do right now.

We would also like the source files for the design. We don’t have Corel Draw, but can work with any files produced in Adobe Creative Suite products.

Target Market(s)

Owners of residential apartments

Industry/Entity Type

Non-Profit

Requirements
Must have
• Design must be complimentary to our new website design at www.trv.org.au so we can establish consistent branding.
• Any fonts used must be freely avalaible standard fonts used in Microsoft Word

```html
<!DOCTYPE html>
<html lang="en">
<head>
<meta charset="utf-8">
<title>TRV Flyer – The Essentials of Strata Living</title>
<link href="https://fonts.googleapis.com/css2?family=Questrial&family=Josefin+Sans:wght@600;700&display=swap" rel="stylesheet">
<style>
  :root {
    --navy: #253374;
    --gold: #b79a32;
    --ink: #1d1d1b;
    --grey: #8c8c8c;
    --frame: #e4e4e4;
    --paper: #ffffff;
  }
  * { margin: 0; padding: 0; box-sizing: border-box; }
  html, body { width: 848px; height: 1200px; overflow: hidden; background: var(--paper); }
  .flyer { position: relative; width: 848px; height: 1200px; overflow: hidden; font-family: "Questrial", "Century Gothic", sans-serif; color: var(--grey); }
  .frames { position: absolute; inset: 0; }
  .brand { position: absolute; top: 56px; left: 0; width: 848px; display: flex; justify-content: center; align-items: center; gap: 12px; }
  .brand-mark { width: 40px; height: 40px; background: var(--gold); }
  .brand-name { font-family: "Questrial", sans-serif; color: var(--navy); font-size: 18px; line-height: 17px; letter-spacing: 1px; text-transform: uppercase; }
  .title { position: absolute; top: 146px; left: 0; width: 848px; text-align: center; font-family: "Josefin Sans", sans-serif; font-weight: 700; font-size: 30px; line-height: 36px; letter-spacing: 2px; color: var(--ink); }
  .date-band { position: absolute; top: 236px; left: 0; width: 848px; height: 52px; }
  .date-band span { position: absolute; left: 216px; top: 9px; font-family: "Josefin Sans", sans-serif; font-weight: 700; font-size: 29px; letter-spacing: 3px; color: #fff; }
  .intro { position: absolute; top: 318px; left: 66px; width: 740px; font-size: 13px; line-height: 18.5px; }
  .intro p { margin-bottom: 0; }
  .intro .gap { margin-top: 18px; }
  .intro .gap-lg { margin-top: 19px; }
  .intro strong { font-weight: normal; font-family: "Josefin Sans", sans-serif; font-weight: 700; font-size: 15px; color: #7d7d7d; }
  .register-band { position: absolute; top: 617px; left: 0; width: 430px; height: 30px; }
  .register-band span { position: absolute; left: 66px; top: 3px; font-family: "Josefin Sans", sans-serif; font-weight: 700; font-size: 21px; color: #fff; }
  .programme { position: absolute; top: 670px; left: 66px; width: 700px; font-size: 13px; line-height: 18.5px; }
  .programme h2 { font-size: 12px; font-weight: normal; color: #6f6f6f; font-family: "Josefin Sans", sans-serif; font-weight: 700; }
  .schedule { position: absolute; top: 752px; left: 101px; width: 625px; border-collapse: collapse; font-size: 11.5px; text-align: center; color: var(--grey); }
  .schedule th { font-family: "Josefin Sans", sans-serif; font-weight: 700; font-size: 14px; color: #7d7d7d; height: 22px; }
  .schedule td { border: 1.5px solid var(--gold); line-height: 18px; padding: 2px 6px; }
  .schedule .period { width: 259px; font-family: "Josefin Sans", sans-serif; font-weight: 700; font-size: 14px; color: #7d7d7d; }
  .schedule .topic { width: 150px; }
  .theme { position: absolute; top: 928px; left: 66px; width: 720px; font-size: 13px; line-height: 18.6px; }
  .call { position: absolute; top: 1118px; left: 0; width: 848px; text-align: center; font-family: "Josefin Sans", sans-serif; font-weight: 700; font-size: 17px; line-height: 23px; color: var(--ink); letter-spacing: .3px; }
</style>
</head>
<body>
<main class="flyer">
  <svg class="frames" width="848" height="1200" viewBox="0 0 848 1200" aria-hidden="true">
    <g fill="none" stroke="var(--frame)" stroke-width="1">
      <polyline points="0,156 175,156 175,0"/>
      <rect x="-1" y="57" width="64" height="209"/>
      <rect x="653" y="397" width="200" height="209"/>
      <rect x="542" y="508" width="210" height="209"/>
      <rect x="50" y="954" width="210" height="209"/>
      <polyline points="0,1065 148,1065 148,1200"/>
    </g>
  </svg>

  <header class="brand">
    <div class="brand-mark"></div>
    <div class="brand-name">Tower<br>Residents<br>Voice</div>
  </header>

  <h1 class="title">- The Essentials of Strata Living –<br>“What Every Owner Needs to Know”</h1>

  <div class="date-band">
    <svg width="848" height="52" viewBox="0 0 848 52" aria-hidden="true"><polygon points="92,0 848,0 848,52 140,52" fill="var(--gold)"/></svg>
    <span>12th and 26th June 2010</span>
  </div>

  <section class="intro">
    <p>This workshop is for owners in strata apartments who want to learn more about</p>
    <p>• getting the best out of apartment living</p>
    <p>• protecting their home and their investment</p>
    <p class="gap"><strong>AND</strong> particularly for</p>
    <p class="gap">• executive committee members to know their rights and responsibilities in managing their strata scheme</p>
    <p class="gap"><strong>Location:</strong> Bayside Club, 24 Marina Parade, Harbour Point 2061</p>
    <p class="gap"><strong>Dates:</strong> The workshop will run twice – on 12th June and 26th June 2010</p>
    <p class="gap"><strong>Time:</strong> 10.00 am to 4.00 pm.</p>
    <p class="gap"><strong>Cost:</strong> $60.00, which includes morning tea and lunch. The maximum number of participants for each workshop is 60.</p>
  </section>

  <div class="register-band">
    <svg width="430" height="30" viewBox="0 0 430 30" aria-hidden="true"><polygon points="0,0 427,0 390,30 0,30" fill="var(--navy)"/></svg>
    <span>Register at www.trv.org.au</span>
  </div>

  <section class="programme">
    <h2>Programme:</h2>
    <p>The day will comprise four sessions, each facilitated by a specialist. In each session the speaker will provide relevant information and set the topics for group work; participants will break into groups and work up solutions to each topic; and the groups will compare outcomes.</p>
  </section>

  <table class="schedule">
    <thead>
      <tr><th></th><th>Topic</th><th>Speaker</th></tr>
    </thead>
    <tbody>
      <tr><td class="period" rowspan="2">Morning</td><td class="topic">Governance</td><td>Martin Hale, strata lawyer</td></tr>
      <tr><td class="topic">Management</td><td>Peter Lowden, seasoned<br>former chairperson and<br>executive committee member</td></tr>
      <tr><td class="period" rowspan="2">Afternoon</td><td class="topic">Financials</td><td>David Carrow, accountant</td></tr>
      <tr><td class="topic">Physicality</td><td>Simon Ferrante, facilities manager</td></tr>
    </tbody>
  </table>

  <section class="theme">
    <p>The day’s theme will be:</p>
    <p>Gina is a new owner in her building called Utopia Tower. She notices some management processes which to her seem strange. She is elected to the executive committee and finds that the developer has retained more control than she realised - the service providers have long-term and onerous contracts, and she doesn’t seem to be able to exert enough influence. What does the law require her to do, as a committee member? How does she influence good management processes? The finances seem to be out of control, so how can she fix them so she doesn’t pay inflated levies each year and lose value on her investment? ... and then the neighbour above her apartment installs a timber floor and she has noise problems ... and the building seems to have a lot of defects ...........</p>
  </section>

  <p class="call">ENROLL NOW - LEARN A LOT - HAVE SOME FUN AS WELL - SHARE EXPERIENCES -<br>FIND OUT HOW TRV CAN HELP YOU IN THE LONGER TERM.</p>
</main>
</body>
</html>
```